business card - Helicopter Flight Services, Flight School, etc.

We need a business card design for a new helicopter service.

We offer Helicopter Flight Services, Aerial Filming & Photography, Flight School, and Helicopter Tours. In that order.

Summit BladeLine, Inc.
Harold Tebbets
SummitBladeline@Mailvane.com
555-014-2786

Based at the Corvell Airport in Van Nuys, CA. The final design should communicate integrity and safety. Pictures or logos at your discretion.

Card back side - surprise me.

```html
<!DOCTYPE html>
<html lang="en">
<head>
<meta charset="utf-8">
<title>Summit BladeLine, Inc. — Business Card</title>
<link rel="stylesheet" href="https://fonts.googleapis.com/css2?family=Source+Sans+3:wght@400;600&display=swap">
<style>
  :root {
    --stage: #000000;
    --card-light: #f2f2f2;
    --card-blue: #0590f9;
    --brand-blue: #1a8cf0;
    --ink: #1c1c1c;
    --white: #ffffff;
  }
  * { margin: 0; padding: 0; box-sizing: border-box; }
  html, body {
    width: 1200px; height: 900px; overflow: hidden;
    background: var(--stage);
    font-family: "Source Sans 3", "Myriad Pro", Arial, sans-serif;
  }
  .stage { position: relative; width: 1200px; height: 900px; }

  .card { position: absolute; top: 200px; width: 310px; height: 502px; }
  .card--front {
    left: 265px; background: var(--card-light);
    border-radius: 56px 0 56px 0;
  }
  .card--back {
    left: 640px; width: 309px; background: var(--card-blue);
    border-radius: 0 56px 0 56px;
  }

  .wordmark {
    position: absolute; display: flex; align-items: center; gap: 12px;
    font-weight: 600; font-size: 15px; line-height: 18px; letter-spacing: 0.06em;
    text-transform: uppercase;
  }
  .card--front .wordmark { left: 72px; top: 60px; color: var(--brand-blue); }
  .card--back .wordmark { left: 44px; top: 62px; color: var(--white); font-size: 16px; line-height: 19px; }
  .wordmark__dot { width: 34px; height: 34px; border-radius: 50%; flex: none; }
  .card--front .wordmark__dot { background: var(--brand-blue); }
  .card--back .wordmark__dot { background: var(--white); }

  .holder {
    position: absolute; left: 25px; top: 373px;
    font-size: 19px; font-weight: 600; color: var(--brand-blue);
  }
  .contact { position: absolute; left: 25px; top: 419px; list-style: none; }
  .contact li {
    display: flex; align-items: center; gap: 9px;
    font-size: 14px; color: var(--ink); height: 21px;
  }
  .contact svg { width: 10px; height: 10px; fill: var(--brand-blue); flex: none; }

  .services { position: absolute; left: 27px; top: 339px; list-style: none; }
  .services li {
    display: flex; align-items: center; gap: 7px;
    font-size: 14px; color: var(--white); height: 28.5px;
  }
  .services li::before {
    content: ""; width: 9px; height: 9px; border-radius: 50%; background: var(--white);
  }
</style>
</head>
<body>
<main class="stage">
  <section class="card card--front" aria-label="Card front">
    <div class="wordmark">
      <span class="wordmark__dot"></span>
      <span>Summit<br>BladeLine<br>Inc.</span>
    </div>
    <p class="holder">Harold Tebbets</p>
    <ul class="contact">
      <li>
        <svg viewBox="0 0 10 10" aria-hidden="true"><path d="M2 0.5 L3.6 2.6 L2.7 3.6 C3.3 5 4.8 6.6 6.3 7.3 L7.4 6.3 L9.5 7.9 L8.4 9.5 C4.5 9.3 0.7 5.5 0.5 1.6 Z"/></svg>
        555-014-2786
      </li>
      <li>
        <svg viewBox="0 0 10 10" aria-hidden="true"><path d="M0.5 2 H9.5 V8 H0.5 Z M0.9 2.4 L5 5.4 L9.1 2.4" stroke="#f2f2f2" stroke-width="0.8"/></svg>
        SummitBladeline@Mailvane.com
      </li>
    </ul>
  </section>

  <section class="card card--back" aria-label="Card back">
    <div class="wordmark">
      <span class="wordmark__dot"></span>
      <span>Summit<br>BladeLine<br>Inc.</span>
    </div>
    <ul class="services">
      <li>Flight School</li>
      <li>Helicopter Tours</li>
      <li>Helicopter Flight Services</li>
      <li>Aerial Filming &amp; Photography</li>
    </ul>
  </section>
</main>
</body>
</html>
```